Create/Design Awesome TorvinaRX Label for Pain Cream

I need a label design for a pain relief cream to be sold online in a highly competitve space(brivo). Therefore the label needs to be a killer and really jump off the page.
I am a RN so I want it to have a bit of a clinical look while still embracing an all natural product (blend east & west medicine?). It will be on a small solid white tub (3oz). The look should communicate pain alleviation/relief, all natural feel good, cooling soothing. The product color is like azure/light blue so may could incorporate that.

You can view the competition here: https://www.brivo-shop.example/s/ref=nb_sb_ss_i_2_5?url=search-alias%3Daps&field-keywords=pain+relief+cream&sprefix=pain+%2Caps%2C163

You can see some of my other products here: http://www.brivo-shop.example/s?marketplaceID=QLMRTZPWY4HUS&me=KOB8J2D3XRUMP&merchant=KOB8J2D3XRUMP&redirect=true

TorvinaRX All Natural
Pain Relief
Inflammation
Formulation

with Arnica, B6 & MSM

This should be wording on front of label. May rearrange or add to? Can use template boxes on sides.

Template & Product highlights attached

PS: Hoping on creative & patient designer who can help me make this really awesome. Looking for long term relationship as I have many other products in the works.

Think clinical/professional but still friendly. Like something your doctor od pharmacist may give you. Added Sunday, December 6, 2015

Reason: I was just now able to complete brief with more information. Want to give ample time for best designs.

Target Market(s)

35-90 years old, male and females

Industry/Entity Type

Medical

Colors
85acd3
3377b5
fbee3f
fbed22
ec1f27
ffffff
9bcb3c

Requirements
Must have
• Bright, colorful, clinical all natural look.
Nice to have
• maybe some images of musculo-sketekal (spine, Knees, elbows) in background?
Should not have
• Please do not copy front wording of template

```html
<!DOCTYPE html>
<html lang="en">
<head>
<meta charset="utf-8">
<title>TorvinaRX Pain Relief Cream Label</title>
<link rel="stylesheet" href="https://fonts.googleapis.com/css2?family=Russo+One&family=Great+Vibes&display=swap">
<style>
  :root {
    --backdrop: #dcdcdc;
    --aqua-light: #3fd6e8;
    --aqua-mid: #12b6d6;
    --aqua-deep: #0a8fb8;
    --brand-green: #9bcb3c;
    --ink-white: #ffffff;
    --ink-dark: #1a1f26;
    --dot-field: #1a5f78;
  }
  * { margin: 0; padding: 0; box-sizing: border-box; }
  html, body {
    width: 1200px;
    height: 800px;
    overflow: hidden;
    background: var(--backdrop);
  }
  .canvas {
    position: relative;
    width: 1200px;
    height: 800px;
  }
  .label {
    position: absolute;
    left: 128px;
    top: 117px;
    width: 945px;
    height: 567px;
    border-radius: 28px;
    overflow: hidden;
    background: linear-gradient(160deg, var(--aqua-light) 0%, var(--aqua-mid) 55%, var(--aqua-deep) 100%);
  }
  .label-art {
    position: absolute;
    inset: 0;
    width: 100%;
    height: 100%;
  }
  .brand-name {
    position: absolute;
    left: 160px;
    top: 118px;
    font-family: "Russo One", sans-serif;
    font-weight: 400;
    font-size: 116px;
    line-height: 1;
    color: var(--brand-green);
  }
  .claims {
    position: absolute;
    left: 205px;
    top: 318px;
    list-style: none;
    font-family: "Russo One", sans-serif;
    font-style: italic;
    font-size: 34px;
    line-height: 44px;
    color: var(--ink-white);
  }
  .net-weight {
    position: absolute;
    left: 505px;
    top: 440px;
    font-family: "Russo One", sans-serif;
    font-style: italic;
    font-size: 32px;
    color: var(--ink-dark);
  }
  .ingredients {
    position: absolute;
    left: 200px;
    top: 512px;
    font-family: "Great Vibes", cursive;
    font-size: 22px;
    color: var(--ink-dark);
  }
</style>
</head>
<body>
<div class="canvas">
  <section class="label">
    <svg class="label-art" viewBox="0 0 945 567" xmlns="http://www.w3.org/2000/svg">
      <defs>
        <linearGradient id="sweepTone" x1="0" y1="0" x2="1" y2="0">
          <stop offset="0" stop-color="#ffffff" stop-opacity="0"/>
          <stop offset="0.5" stop-color="#ffffff" stop-opacity="0.22"/>
          <stop offset="1" stop-color="#ffffff" stop-opacity="0"/>
        </linearGradient>
      </defs>
      <path d="M0 150 C 250 60, 520 40, 945 110 L 945 220 C 600 150, 300 170, 0 260 Z"
            fill="url(#sweepTone)" role="img" aria-label="Soft flowing light wave lines"/>
      <circle cx="20" cy="30" r="90" fill="var(--dot-field)" opacity="0.55"
              role="img" aria-label="Halftone dot sphere decoration"/>
      <circle cx="810" cy="450" r="195" fill="var(--dot-field)" opacity="0.55"
              role="img" aria-label="Large halftone dot sphere decoration"/>
    </svg>

    <h1 class="brand-name">TorvinaRX</h1>
    <ul class="claims">
      <li>All Natural</li>
      <li>Pain Relief</li>
      <li>Inflammation</li>
      <li>Formulation</li>
    </ul>
    <p class="net-weight">3 oz</p>
    <p class="ingredients">with Arnica, B6 &amp; MSM</p>
  </section>
</div>
</body>
</html>
```